RIVERtide Press Needs a Book Cover Design

We need a book cover design for an inspirational, motivational nugget book. It's another part of a series of small 1-paragraph chapter books with lots of quotes. It is a spiritual book and we would like to see designs that depict peace through a storm. The final design should communicate peace or calm through violent storms of life--adversity, setbacks, and sorrow.
The book size is 5.5 x 8.5 ins and the number of pages is 96.
Updates
Project Deadline Extended
Reason: To be able to allow for more submissions.
Target Market(s)
General reading audience
Look and feel
Each slider illustrates characteristics of the customer's brand and the style your logo design should communicate.

```html
<!DOCTYPE html>
<html lang="en">
<head>
<meta charset="UTF-8">
<title>Peace Through The Storms — Book Cover</title>
<link rel="stylesheet" href="https://fonts.googleapis.com/css2?family=Lexend:wght@300;600&display=swap">
<style>
  :root {
    --backdrop: #435a82;
    --sky-white: #f6f7fb;
    --sky-haze: #dfe3f0;
    --sky-blush: #f1d9e6;
    --cloud-lilac: #b8bde3;
    --storm-blue: #4f7fd6;
    --deep-blue: #3a6cd0;
    --ink: #111114;
  }
  * { margin: 0; padding: 0; box-sizing: border-box; }
  html, body {
    width: 981px;
    height: 1200px;
    overflow: hidden;
    background: var(--backdrop);
  }
  .canvas {
    position: relative;
    width: 981px;
    height: 1200px;
    display: flex;
    align-items: center;
    justify-content: center;
  }
  .cover {
    position: relative;
    width: 660px;
    height: 1020px;
    overflow: hidden;
  }
  .cover-sky {
    position: absolute;
    inset: 0;
    background:
      radial-gradient(ellipse 55% 30% at 85% 58%, var(--sky-blush) 0%, transparent 70%),
      radial-gradient(ellipse 70% 35% at 50% 20%, var(--sky-white) 0%, transparent 75%),
      radial-gradient(ellipse 60% 25% at 20% 50%, var(--cloud-lilac) 0%, transparent 80%),
      linear-gradient(180deg,
        var(--sky-white) 0%,
        var(--sky-haze) 35%,
        var(--cloud-lilac) 62%,
        #9fb3e6 80%,
        var(--storm-blue) 93%,
        var(--deep-blue) 100%);
  }
  .cover-text {
    position: absolute;
    inset: 0;
    font-family: "Lexend", sans-serif;
    color: var(--ink);
  }
  .title {
    position: absolute;
    top: 352px;
    left: 0;
    right: 0;
    text-align: center;
    font-weight: 600;
    font-size: 122px;
    line-height: 1;
    letter-spacing: 1px;
    padding-left: 70px;
  }
  .subtitle {
    position: absolute;
    top: 480px;
    left: 0;
    right: 0;
    text-align: center;
    font-weight: 300;
    font-size: 33px;
    line-height: 1;
    padding-left: 20px;
  }
  .author {
    position: absolute;
    top: 903px;
    left: 0;
    right: 0;
    text-align: center;
    font-weight: 300;
    font-size: 28px;
    line-height: 1;
  }
</style>
</head>
<body>
  <main class="canvas">
    <article class="cover">
      <div class="cover-sky" role="img" aria-label="Photograph of a sky above soft clouds with lightning flashing through them, white light above and blue storm clouds below"></div>
      <div class="cover-text">
        <h1 class="title">PEACE</h1>
        <p class="subtitle">Through The Storms</p>
        <p class="author">Author’s Name</p>
      </div>
    </article>
  </main>
</body>
</html>
```